Kelvo Tech Oz Business card revamp

We are looking to revamp our business card design. We are hoping to change our colours to dark navey blue, gray, white and black but are open to keeping the same if a good design is submited. We are after somthing a bit differnt not just boring business card. I have attached a copy of our current card. We Want to keep the same logo design which i have attached a few to hopfully help you in this process. We are after a design that can be personalized to separate 4 people

Colors
0455a3
ffffff
000000
cbcbcb

Requirements
Must have
• Kelvo Tech Logo, address 3/41 Mallory Court, Wexhill 4218, phone number, Name and position

```html
<!DOCTYPE html>
<html lang="en">
<head>
<meta charset="utf-8">
<title>Kelvo Tech – Business Card</title>
<link href="https://fonts.googleapis.com/css2?family=Montserrat:wght@400;500;600;800&display=swap" rel="stylesheet">
<style>
  :root {
    --blue: #1559ad;
    --blue-light: #1c7fcf;
    --navy-text: #1b3f6e;
    --orange: #f07a22;
    --white: #ffffff;
    --gray: #cbcbcb;
    --backdrop: #dcdcdc;
  }
  * { margin: 0; padding: 0; box-sizing: border-box; }
  html, body { width: 1200px; height: 800px; overflow: hidden; }
  body {
    background: radial-gradient(ellipse at 50% 35%, #ececec 0%, var(--backdrop) 60%, #cfcfcf 100%);
    font-family: "Montserrat", sans-serif;
    display: flex;
    align-items: center;
    justify-content: center;
    gap: 60px;
  }
  .card {
    width: 520px;
    height: 297px;
    background: var(--white);
    position: relative;
    overflow: hidden;
    box-shadow: 0 14px 30px rgba(0,0,0,0.18);
  }
  .brand {
    display: flex;
    align-items: center;
    gap: 10px;
  }
  .brand-dot {
    width: 30px; height: 30px;
    border-radius: 50%;
    background: var(--orange);
  }
  .brand-name {
    font-weight: 800;
    font-size: 30px;
    color: var(--blue);
    letter-spacing: -0.5px;
  }
  /* Front side */
  .card-front .brand {
    position: absolute;
    top: 95px; left: 0; right: 0;
    justify-content: center;
  }
  .card-front .brand-name { font-size: 38px; }
  .card-front .brand-dot { width: 38px; height: 38px; }
  .web-band {
    position: absolute;
    left: 0; right: 0; bottom: 0;
    height: 48px;
    background: var(--blue);
    color: var(--white);
    font-size: 13px;
    letter-spacing: 7px;
    display: flex;
    align-items: center;
    justify-content: center;
  }
  /* Back side */
  .card-back .brand {
    position: absolute;
    top: 80px; left: 26px;
  }
  .card-back .brand-name { font-size: 24px; }
  .card-back .brand-dot { width: 24px; height: 24px; }
  .contact {
    position: absolute;
    top: 26px; left: 290px;
    list-style: none;
    color: var(--navy-text);
    font-size: 11.5px;
    line-height: 1.2;
    letter-spacing: 0.5px;
  }
  .contact li {
    display: flex;
    align-items: center;
    gap: 12px;
    height: 50px;
  }
  .contact svg { width: 14px; height: 14px; flex: none; fill: var(--navy-text); }
  .gray-rule {
    position: absolute;
    left: 0; right: 0;
    top: 180px;
    height: 7px;
    background: var(--gray);
  }
  .name-band {
    position: absolute;
    left: 0; right: 0; bottom: 0;
    top: 187px;
    background: linear-gradient(120deg, var(--blue) 0%, var(--blue-light) 40%, var(--blue) 80%);
    color: var(--white);
    text-align: center;
    padding-top: 28px;
  }
  .person-name {
    font-weight: 600;
    font-size: 24px;
    letter-spacing: 1.5px;
  }
  .person-role {
    font-size: 10.5px;
    letter-spacing: 6px;
    margin-top: 6px;
  }
</style>
</head>
<body>
  <section class="card card-front">
    <div class="brand">
      <span class="brand-dot"></span>
      <span class="brand-name">Kelvo Tech</span>
    </div>
    <div class="web-band">www.kelvotech.com</div>
  </section>

  <section class="card card-back">
    <div class="brand">
      <span class="brand-dot"></span>
      <span class="brand-name">Kelvo Tech</span>
    </div>
    <ul class="contact">
      <li>
        <svg viewBox="0 0 24 24" aria-hidden="true"><path d="M6.6 10.8a15.1 15.1 0 0 0 6.6 6.6l2.2-2.2c.3-.3.7-.4 1-.2 1.1.4 2.3.6 3.6.6.6 0 1 .4 1 1V20c0 .6-.4 1-1 1A17 17 0 0 1 3 4c0-.6.4-1 1-1h3.5c.6 0 1 .4 1 1 0 1.3.2 2.5.6 3.6.1.3 0 .7-.2 1z"/></svg>
        <span>+1 555 210 4831<br>+1 555 382 9176</span>
      </li>
      <li>
        <svg viewBox="0 0 24 24" aria-hidden="true"><path d="M2 5h20v14H2z M3.5 6.5 12 13l8.5-6.5" stroke="#fff" stroke-width="1.4"/></svg>
        <span>marlene.j.c@kelvotech.com</span>
      </li>
      <li>
        <svg viewBox="0 0 24 24" aria-hidden="true"><path d="M12 2a7 7 0 0 0-7 7c0 5.2 7 13 7 13s7-7.8 7-13a7 7 0 0 0-7-7zm0 9.5A2.5 2.5 0 1 1 12 6.5a2.5 2.5 0 0 1 0 5z"/></svg>
        <span>3/41 Mallory Court,<br>Wexhill 4218</span>
      </li>
    </ul>
    <div class="gray-rule"></div>
    <div class="name-band">
      <div class="person-name">MARLENE J. CORVIN</div>
      <div class="person-role">PRESIDENT</div>
    </div>
  </section>
</body>
</html>
```